Business cards/stationary for physician office
Using existing logo
Bright & Fun-filled
Paul Verner, M.D.
Radiologist
Cedarpoint Imaging, LLC.
48 Quill Ridge Lane
Montgomery, TX 77490
office@brakwell-mail.net
www.cedarpointimaging-demo.com
Will contact the winning designer with actual contact info to replace above text. Please not website has not been updated with new logo, so make sure to use provided logo files.
Logo files
Logo file horizontal

```html
<!DOCTYPE html>
<html lang="en">
<head>
<meta charset="utf-8">
<title>Cedarpoint Imaging – Business Card</title>
<link rel="stylesheet" href="https://fonts.googleapis.com/css2?family=PT+Serif:wght@400;700&display=swap">
<style>
  :root {
    --page-bg: #e9e6e1;
    --card-white: #ffffff;
    --brand-blue: #2d5a98;
    --swoosh-grey: #b9bcc2;
    --marker-grey: #8a97a8;
    --text-light: #ffffff;
  }
  * { margin: 0; padding: 0; box-sizing: border-box; }
  html, body {
    width: 1200px; height: 780px; overflow: hidden;
    background: var(--page-bg);
  }
  .canvas { position: relative; width: 1200px; height: 780px; }
  .card {
    position: absolute; left: 100px; top: 90px;
    width: 1000px; height: 600px;
    border-radius: 30px; overflow: hidden;
    background: var(--card-white);
    box-shadow: 0 8px 24px rgba(0,0,0,0.15);
    font-family: "PT Serif", Georgia, serif;
  }
  .card-shapes { position: absolute; inset: 0; }
  .brand {
    position: absolute; left: 50px; top: 240px;
    display: flex; align-items: center; gap: 16px;
  }
  .brand-marker {
    width: 56px; height: 56px; border-radius: 50%;
    background: var(--marker-grey); flex: none;
  }
  .brand-name {
    color: var(--brand-blue); font-weight: 400;
    font-size: 40px; line-height: 1.1; white-space: nowrap;
  }
  .contact {
    position: absolute; right: 60px; top: 118px;
    color: var(--text-light); text-align: right;
  }
  .contact-name { font-size: 38px; font-weight: 700; line-height: 1.1; }
  .contact-title { font-size: 27px; margin-bottom: 40px; }
  .contact-address { font-size: 25px; line-height: 1.3; margin-bottom: 26px; }
  .contact-line {
    display: flex; justify-content: flex-end; align-items: center;
    gap: 14px; font-size: 25px; line-height: 1.32;
  }
  .contact-line svg { width: 24px; height: 24px; flex: none; }
  .contact-web { margin-top: 6px; }
</style>
</head>
<body>
<main class="canvas">
  <section class="card">
    <svg class="card-shapes" viewBox="0 0 1000 600" preserveAspectRatio="none" aria-hidden="true">
      <path class="swoosh" fill="var(--swoosh-grey)"
            d="M0 430 C 170 470, 400 420, 560 300 C 420 400, 200 445, 0 455 Z"/>
      <path class="blue-field" fill="var(--brand-blue)"
            d="M640 0 L1000 0 L1000 600 L0 600 L0 470 C 220 475, 430 430, 520 300 C 590 200, 560 70, 640 0 Z"/>
    </svg>

    <div class="brand">
      <div class="brand-marker"></div>
      <div class="brand-name">Cedarpoint Imaging</div>
    </div>

    <div class="contact">
      <div class="contact-name">Paul Verner, M.D.</div>
      <div class="contact-title">Radiologist</div>
      <div class="contact-address">48 Quill Ridge Lane<br>Montgomery, TX 77490</div>

      <div class="contact-line">936-555-0148
        <svg viewBox="0 0 24 24"><path fill="#fff" d="M6.6 10.8a15 15 0 0 0 6.6 6.6l2.2-2.2c.3-.3.7-.4 1-.2 1.1.4 2.3.6 3.6.6.6 0 1 .4 1 1V20c0 .6-.4 1-1 1A17 17 0 0 1 3 4c0-.6.4-1 1-1h3.5c.6 0 1 .4 1 1 0 1.3.2 2.5.6 3.6.1.3 0 .7-.2 1z"/></svg>
      </div>
      <div class="contact-line">936-555-0162
        <svg viewBox="0 0 24 24"><rect x="6" y="2" width="12" height="20" rx="2" fill="#fff"/><rect x="8" y="5" width="8" height="12" fill="var(--brand-blue)"/></svg>
      </div>
      <div class="contact-line">936-555-0177
        <svg viewBox="0 0 24 24"><rect x="7" y="3" width="10" height="6" fill="#fff"/><rect x="3" y="9" width="18" height="9" rx="1.5" fill="#fff"/><rect x="7" y="15" width="10" height="6" fill="#fff" stroke="var(--brand-blue)" stroke-width="1.2"/></svg>
      </div>
      <div class="contact-line">office@brakwell-mail.net
        <svg viewBox="0 0 24 24"><rect x="2" y="5" width="20" height="14" rx="1.5" fill="#fff"/><path d="M3 6l9 7 9-7" fill="none" stroke="var(--brand-blue)" stroke-width="1.6"/></svg>
      </div>
      <div class="contact-line contact-web">www.cedarpointimaging-demo.com
        <svg viewBox="0 0 24 24"><circle cx="12" cy="12" r="9.5" fill="none" stroke="#fff" stroke-width="1.8"/><ellipse cx="12" cy="12" rx="4" ry="9.5" fill="none" stroke="#fff" stroke-width="1.5"/><path d="M2.5 12h19" stroke="#fff" stroke-width="1.5"/></svg>
      </div>
    </div>
  </section>
</main>
</body>
</html>
```